BrightHarbor Flowchart Marketing Flyer

We are an MSP IT company. We have created a flowchart that we would like jazzed up to use in marketing new customers. The flowchart is a visual for prospective clients to see, in a simple way, what our process is. The flowchart should be 8.5"x11". We do not want the template of the flowchart altered (no boxes moved around) but would like something visually appealing and clean looking. Our office colors are lime green, royal blue, with accent colors of orange and purple. We would like the colors incorporated into the design. The design should be modern. This flyer is not going to be mass mailed. It will be handed to a prospective client in a face to face meeting.
Updates

I have uploaded our company logo to my brief in a couple of formats. One of the designers requested this. Great idea! I apologize for not providing it to begin with - it's my first time using this Website and the first time I have been assigned a project.

I was not able to view over the weekend as I did not have access to my work computer. Also need to review with the rest of management team on Thursday 6/28

Target Market(s)

Potential clients for an MSP IT company

Industry/Entity Type

It Company

Requirements
Must have
• The template itself we don't want changed. In other words we don't want the boxes moved around.
Nice to have
• Text, lines, shading and color of boxes can be changed. Not all colors mentioned in the brief need to be used. Would like it easy on the eye.

```html
<!DOCTYPE html>
<html lang="en">
<head>
<meta charset="utf-8">
<title>BrightHarbor Process</title>
<link href="https://fonts.googleapis.com/css2?family=Barlow:wght@500;600;700&family=Montserrat:wght@500;600&display=swap" rel="stylesheet">
<style>
  :root {
    --royal-blue: #1160a8;
    --header-grey: #e6e7e8;
    --page-bg: #eceef0;
    --orange-start: #ec6526;
    --orange-end: #f59e22;
    --purple-top: #8a3b99;
    --purple-bottom: #71308d;
    --lime-start: #9dc53f;
    --lime-end: #7dbd45;
    --lime-fold: #5f9a2c;
    --rule-grey: #c4c5c7;
    --ink: #1f2a33;
    --white: #ffffff;
  }
  html, body {
    margin: 0;
    width: 1200px;
    height: 1200px;
    overflow: hidden;
    background: var(--page-bg);
  }
  .flyer {
    position: absolute;
    left: 0;
    top: 136px;
    width: 1200px;
    height: 927px;
    display: block;
  }
  .title { font-family: "Barlow", sans-serif; font-weight: 700; font-size: 50px; fill: var(--white); letter-spacing: 1px; }
  .brand-name { font-family: "Barlow", sans-serif; font-weight: 700; font-size: 30px; fill: var(--royal-blue); }
  .step-label { font-family: "Montserrat", sans-serif; font-weight: 500; font-size: 17px; fill: var(--white); text-anchor: middle; }
  .bullet { font-family: "Barlow", sans-serif; font-weight: 600; font-size: 11px; fill: var(--ink); }
  .banner-text { font-family: "Barlow", sans-serif; font-weight: 600; font-size: 18px; fill: var(--white); }
  .pill-text { font-family: "Montserrat", sans-serif; font-weight: 500; font-size: 13px; fill: var(--ink); text-anchor: middle; letter-spacing: 0.5px; }
  .rule { stroke: var(--rule-grey); stroke-width: 2.5; fill: none; }
  .cycle-arc { stroke: var(--white); stroke-width: 2; fill: none; }
</style>
</head>
<body>
<svg class="flyer" viewBox="199 289 1102 851" xmlns="http://www.w3.org/2000/svg">
  <defs>
    <linearGradient id="orange-fill" x1="0" x2="1" y1="0" y2="0">
      <stop offset="0" stop-color="var(--orange-start)"/>
      <stop offset="1" stop-color="var(--orange-end)"/>
    </linearGradient>
    <linearGradient id="purple-fill" x1="0" x2="0" y1="0" y2="1">
      <stop offset="0" stop-color="var(--purple-top)"/>
      <stop offset="1" stop-color="var(--purple-bottom)"/>
    </linearGradient>
    <linearGradient id="lime-fill" x1="0" x2="1" y1="0" y2="0">
      <stop offset="0" stop-color="var(--lime-start)"/>
      <stop offset="1" stop-color="var(--lime-end)"/>
    </linearGradient>
    <filter id="pill-shadow" x="-10%" y="-20%" width="120%" height="150%">
      <feDropShadow dx="0" dy="2" stdDeviation="1.5" flood-color="#000" flood-opacity="0.3"/>
    </filter>
  </defs>

  <!-- sheet -->
  <rect class="sheet" x="199" y="289" width="1102" height="851" fill="var(--white)"/>

  <!-- header -->
  <g class="header">
    <polygon points="199,317 1020,317 975,412 199,412" fill="var(--royal-blue)"/>
    <polygon points="1031,317 1301,317 1301,412 987,412" fill="var(--header-grey)"/>
    <text class="title" x="236" y="382">BRIGHTHARBOR PROCESS</text>
    <g class="brand">
      <circle cx="1112" cy="363" r="13" fill="var(--royal-blue)"/>
      <text class="brand-name" x="1134" y="374">Corevia</text>
    </g>
  </g>

  <!-- timeline -->
  <g class="timeline">
    <line class="rule" x1="242" y1="626" x2="876" y2="626"/>
    <circle cx="242" cy="626" r="8" fill="var(--rule-grey)"/>
    <polygon points="874,610 901,626 874,642" fill="var(--rule-grey)"/>
    <g class="node">
      <circle cx="341" cy="627" r="26" fill="var(--white)" stroke="var(--rule-grey)" stroke-width="2.5"/>
      <circle cx="341" cy="627" r="14" fill="url(#orange-fill)"/>
    </g>
    <g class="node">
      <circle cx="558" cy="627" r="26" fill="var(--white)" stroke="var(--rule-grey)" stroke-width="2.5"/>
      <circle cx="558" cy="627" r="14" fill="url(#orange-fill)"/>
    </g>
    <g class="node">
      <circle cx="775" cy="627" r="26" fill="var(--white)" stroke="var(--rule-grey)" stroke-width="2.5"/>
      <circle cx="775" cy="627" r="14" fill="url(#orange-fill)"/>
    </g>
    <line class="rule" x1="341" y1="653" x2="341" y2="672"/>
    <line class="rule" x1="558" y1="653" x2="558" y2="672"/>
    <line class="rule" x1="775" y1="653" x2="775" y2="672"/>
  </g>

  <!-- step 1 -->
  <g class="step">
    <rect x="252" y="672" width="177" height="92" rx="20" fill="url(#orange-fill)"/>
    <text class="step-label" x="338" y="713">ASSESS</text>
    <text class="step-label" x="338" y="736">ALIGNMENT</text>
    <polygon points="440,710 448,718 440,726" fill="var(--rule-grey)"/>
    <polyline class="rule" points="341,764 341,829 252,829 252,900"/>
    <text class="bullet" x="263" y="856">• REVIEW TECHNOLOGY PHILOSOPHY</text>
    <text class="bullet" x="263" y="877">• SHARE PROPRIETARY METHOD</text>
    <text class="bullet" x="263" y="898">• ASSESS ORGANIZATIONAL FIT</text>
  </g>

  <!-- step 2 -->
  <g class="step">
    <rect x="469" y="672" width="177" height="92" rx="20" fill="url(#orange-fill)"/>
    <text class="step-label" x="556" y="726">ON BOARDING</text>
    <polygon points="657,710 665,718 657,726" fill="var(--rule-grey)"/>
    <polyline class="rule" points="558,764 558,829 469,829 469,921"/>
    <text class="bullet" x="480" y="856">• ESTABLISH EXPECTATIONS</text>
    <text class="bullet" x="480" y="877">• SERVICE PROVIDER TRANSITION</text>
    <text class="bullet" x="483" y="898">• CYBERSECURITY REVIEW</text>
    <text class="bullet" x="480" y="919">• BACKUP/PROTECTION STRATEGY</text>
  </g>

  <!-- step 3 -->
  <g class="step">
    <rect x="686" y="672" width="177" height="92" rx="20" fill="url(#orange-fill)"/>
    <text class="step-label" x="775" y="713">30 DAY</text>
    <text class="step-label" x="775" y="736">EVALUATION</text>
    <polygon points="875,710 883,718 875,726" fill="var(--rule-grey)"/>
    <polyline class="rule" points="775,764 775,829 686,829 686,921"/>
    <text class="bullet" x="700" y="856">• DEVELOP IT PLAYBOOK</text>
    <text class="bullet" x="700" y="877">• MAJOR RISK IDENTIFICATION</text>
    <text class="bullet" x="700" y="898">• OBSERVE &amp; DOCUMENT TRENDS</text>
    <text class="bullet" x="700" y="919">• STANDARDS ALIGNMENT PLAN•</text>
  </g>

  <!-- ongoing plan panel -->
  <g class="ongoing-panel">
    <rect x="921" y="490" width="330" height="387" rx="24" fill="url(#purple-fill)"/>
    <polygon points="902,572 921,572 921,586" fill="var(--lime-fold)"/>
    <path d="M902,522 H1259 a6,6 0 0 1 6,6 V566 a6,6 0 0 1 -6,6 H902 Z" fill="url(#lime-fill)"/>
    <text class="banner-text" x="930" y="552">Ongoing Strategic Plan &amp; Execution</text>

    <path class="cycle-arc" d="M1012,633 A40,40 0 0 0 972,671"/>
    <path class="cycle-arc" d="M1167,633 A40,40 0 0 1 1206,671"/>
    <path class="cycle-arc" d="M972,776 A40,40 0 0 0 1012,815"/>
    <path class="cycle-arc" d="M1206,776 A40,40 0 0 1 1167,815"/>

    <g filter="url(#pill-shadow)" fill="var(--white)">
      <rect x="1036" y="614" width="106" height="38" rx="6"/>
      <rect x="937" y="699" width="107" height="39" rx="6"/>
      <rect x="1128" y="702" width="107" height="39" rx="6"/>
      <rect x="1032" y="791" width="107" height="38" rx="6"/>
    </g>
    <text class="pill-text" x="1089" y="638">STRATEGY</text>
    <text class="pill-text" x="990" y="715">RISK</text>
    <text class="pill-text" x="990" y="731">ASSESSMENT</text>
    <text class="pill-text" x="1181" y="718">STANDARDS</text>
    <text class="pill-text" x="1181" y="733">ALIGNMENT</text>
    <text class="pill-text" x="1085" y="815">BUDGET</text>

    <polyline class="rule" points="1085,877 1085,940 921,940 921,1053"/>
    <text class="bullet" x="936" y="968">• DEVELOP &amp; EXECUTE ANNUAL STRATEGIC PLAN</text>
    <text class="bullet" x="936" y="989">• RISK ASSESSMENT, RANKING, MITIGATION</text>
    <text class="bullet" x="936" y="1010">• PRIORITIZE INVESTMENTS</text>
    <text class="bullet" x="936" y="1030">• DEVELOP 5 YEAR BUDGET</text>
    <text class="bullet" x="936" y="1051">• COREVIASOLUTION<tspan dy="-4" font-size="7">TM</tspan><tspan dy="4"> STANDARD ALIGNMENT</tspan></text>
  </g>

  <!-- footer band -->
  <rect class="footer-band" x="199" y="1116" width="1102" height="24" fill="var(--royal-blue)"/>
</svg>
</body>
</html>
```